Business Card Design for The Lending Nook Inc.

We need a business card design for our mortgage company: "The Lending Nook Inc."

Need to have Social Media Account on there as a possibility

Industry/Entity Type

Business

```html
<!DOCTYPE html>
<html lang="en">
<head>
<meta charset="utf-8">
<title>The Lending Nook Inc. — Business Card</title>
<link rel="stylesheet" href="https://fonts.googleapis.com/css2?family=Open+Sans:wght@400;600&family=Varela+Round&display=swap">
<style>
  :root {
    --page: #ffffff;
    --front-dark: #0e0e0e;
    --front-mid: #262626;
    --back-dark: #1c1916;
    --back-mid: #4a423b;
    --back-light: #b9ab98;
    --white: #ffffff;
    --muted: #9c9c9c;
    --title-grey: #8c8482;
    --brand-blue: #1a5cad;
    --social-blue: #2f6fb8;
  }
  * { margin: 0; padding: 0; box-sizing: border-box; }
  html, body {
    width: 1200px; height: 1200px; overflow: hidden;
    background: var(--page);
  }
  .canvas { position: relative; width: 1200px; height: 1200px; }
  .card {
    position: absolute; left: 158px; width: 900px; height: 542px; overflow: hidden;
  }
  .card--front { top: 71px; }
  .card--back { top: 634px; }
  .card__backdrop { position: absolute; inset: 0; }
  .card--front .card__backdrop {
    background: linear-gradient(135deg, var(--front-mid) 0%, var(--front-dark) 45%, #1a1a1a 75%, var(--front-mid) 100%);
  }
  .card--back .card__backdrop {
    background:
      radial-gradient(ellipse 320px 260px at 0% 72%, var(--back-light) 0%, rgba(185,171,152,0) 100%),
      linear-gradient(150deg, var(--back-mid) 0%, var(--back-dark) 55%, #2e2a27 100%);
  }
  .text { position: absolute; white-space: nowrap; font-family: "Open Sans", sans-serif; }
  .company { left: 116px; top: 94px; font-size: 33px; color: var(--white); }
  .contact { left: 115px; top: 152px; font-size: 24px; line-height: 32px; color: var(--muted); }
  .brand-mark {
    position: absolute; border: 4px solid var(--brand-blue); border-radius: 50%;
  }
  .brand-name { color: var(--brand-blue); font-weight: 600; }
  .card--front .brand-mark { left: 425px; top: 103px; width: 92px; height: 92px; }
  .card--front .brand-name { left: 534px; top: 125px; font-size: 31px; }
  .person-name {
    left: 420px; top: 318px; font-family: "Varela Round", sans-serif;
    font-size: 64px; letter-spacing: -2px; color: var(--white); font-weight: 700;
  }
  .person-role {
    left: 498px; top: 388px; font-family: "Varela Round", sans-serif;
    font-size: 28px; letter-spacing: -1px; color: var(--title-grey);
  }
  .card--back .brand-mark { left: 167px; top: 93px; width: 116px; height: 116px; }
  .card--back .brand-name { left: 304px; top: 126px; font-size: 46px; }
  .social { position: absolute; left: 155px; display: flex; align-items: center; }
  .social__dot {
    width: 50px; height: 50px; border-radius: 50%; background: var(--social-blue);
  }
  .social__handle {
    font-family: "Open Sans", sans-serif; font-size: 19px; color: var(--white); margin-left: 48px;
  }
  .social--profile { top: 228px; }
  .social--page { top: 313px; }
  .social--page .social__handle { margin-left: 60px; }
  .social--network { top: 393px; }
</style>
</head>
<body>
<main class="canvas">
  <section class="card card--front">
    <div class="card__backdrop" role="img" aria-label="Dark faceted geometric polygon background"></div>
    <p class="text company">Lending Nook Inc</p>
    <p class="text contact">email@youremail.com<br>www.yourwebsite.com<br>P 123-456-7890</p>
    <span class="brand-mark"></span>
    <p class="text brand-name">The Lending Nook Inc.</p>
    <p class="text person-name">Alex Rowan</p>
    <p class="text person-role">marketing manager</p>
  </section>

  <section class="card card--back">
    <div class="card__backdrop" role="img" aria-label="Bronze and charcoal faceted geometric polygon background"></div>
    <span class="brand-mark"></span>
    <p class="text brand-name">The Lending Nook Inc.</p>
    <div class="social social--profile"><span class="social__dot"></span><span class="social__handle">/your profile</span></div>
    <div class="social social--page"><span class="social__dot"></span><span class="social__handle">/your page</span></div>
    <div class="social social--network"><span class="social__dot"></span></div>
  </section>
</main>
</body>
</html>
```